Business Card Design for a Sound engineer and DJ

We would like a residn of the business card.

Logo must remain the same.
The card is for the owner of the company.
The business card is in Arabic as the company is based in Kuwait.
The company specializes in sound engineering for singers concerts and events and in addition DJ.
The color options is up to the designer but we would like it masculine as the owner is a man.

Target Market(s)

All ages

Industry/Entity Type

Media

Contact Information for Business Card

Name:
Eng. Tarek Halabi
م/طارق حلبي

The name above is in Arabic and English.

Title: General Manager
Mobile: +965 66307852
Office: +965 22486037
Email: info@sawtarin.net

Address:
Office no. 3
1st floor
Almarfa Complex
Rashed AlQeblawi St.
Salmiya
Kuwait

Instagram: @sawtarin
Snap: sawtarin

Requirements
Nice to have
• can we have Instagram icon and snap icon and a phone vector and email?
• Instead of writing the words

```html
<!DOCTYPE html>
<html lang="en">
<head>
<meta charset="utf-8">
<title>Sawtarin Business Card</title>
<link rel="stylesheet" href="https://fonts.googleapis.com/css2?family=Open+Sans:wght@400;600&family=Cairo:wght@400;600&display=swap">
<style>
  :root {
    --stage: #e9e6ef;
    --card: #232225;
    --band-top: #7a3aa6;
    --band-bottom: #9a4dbf;
    --brand: #b99be6;
    --tag: #a58ad6;
    --name: #b556d6;
    --title: #a9a3c4;
    --contact: #8f86e8;
    --address: #1d1a22;
  }
  * { box-sizing: border-box; margin: 0; padding: 0; }
  html, body { width: 1200px; height: 780px; overflow: hidden; }
  body {
    background: var(--stage);
    font-family: "Open Sans", Arial, sans-serif;
    position: relative;
  }
  .card {
    position: absolute;
    background: var(--card);
    border-radius: 4px;
    box-shadow: 0 10px 30px rgba(30, 20, 40, .25);
    overflow: hidden;
  }
  .brand { text-align: center; }
  .brand-mark {
    display: inline-block; width: 12px; height: 12px; border-radius: 50%;
    background: var(--brand); margin-bottom: 14px;
  }
  .brand-name {
    color: var(--brand); font-weight: 400; font-size: 34px;
    letter-spacing: 9px; line-height: 1;
  }
  .brand-tag {
    color: var(--tag); font-size: 10.5px; letter-spacing: 2px;
    margin-top: 10px; text-transform: uppercase;
  }
  .brand-tag-ar {
    color: var(--tag); font-family: "Cairo", sans-serif; font-size: 13px;
    direction: rtl; margin-top: 2px;
  }

  /* Front */
  .card--front { left: 110px; top: 75px; width: 360px; height: 630px; }
  .card--front .band {
    position: absolute; left: 0; right: 0; bottom: 0; height: 96px;
    background: linear-gradient(180deg, var(--band-top), var(--band-bottom));
  }
  .card--front .brand { position: absolute; top: 110px; left: 0; right: 0; }
  .person { position: absolute; top: 285px; left: 40px; right: 30px; }
  .person-name { color: var(--name); font-size: 24px; font-weight: 600; line-height: 1.3; }
  .person-name-ar {
    color: var(--name); font-family: "Cairo", sans-serif; font-size: 18px;
    direction: rtl; text-align: left; line-height: 1.3;
  }
  .person-title { color: var(--title); font-size: 17px; margin-top: 4px; }
  .contacts { position: absolute; top: 405px; left: 40px; list-style: none; }
  .contacts li {
    display: flex; align-items: center; gap: 10px;
    color: var(--contact); font-size: 17px; line-height: 28px;
  }
  .contacts svg { width: 16px; height: 16px; flex: none; }
  .contacts .dot {
    width: 14px; height: 14px; border-radius: 3px; background: var(--contact); flex: none;
  }
  .contacts .dot.round { border-radius: 50%; }
  .contacts .pair { gap: 26px; }
  .contacts .pair span { display: flex; align-items: center; gap: 10px; }

  /* Back */
  .card--back { left: 540px; top: 240px; width: 600px; height: 343px; }
  .card--back .band {
    position: absolute; top: 0; bottom: 0; left: 0; width: 66px;
    background: linear-gradient(90deg, var(--band-top), var(--band-bottom));
  }
  .address {
    position: absolute; left: 33px; top: 50%; width: 320px;
    transform: translate(-50%, -50%) rotate(90deg);
    text-align: center; color: var(--address); font-size: 12.5px; line-height: 19px;
  }
  .address span { display: block; white-space: nowrap; }
  .card--back .brand {
    position: absolute; left: 66px; right: 0; top: 50%; transform: translateY(-50%);
  }
</style>
</head>
<body>
  <section class="card card--front">
    <div class="brand">
      <span class="brand-mark"></span>
      <div class="brand-name">SAWTARIN</div>
      <div class="brand-tag">DJ - Sound Eng. - Lighting</div>
      <div class="brand-tag-ar">دي جي - هندسة صوت - إضاءة</div>
    </div>
    <div class="person">
      <div class="person-name">Eng. Tarek Halabi</div>
      <div class="person-name-ar">م/طارق حلبي</div>
      <div class="person-title">General Manager</div>
    </div>
    <ul class="contacts">
      <li>
        <svg viewBox="0 0 16 16"><rect x="4" y="1" width="8" height="14" rx="1.5" fill="none" stroke="currentColor" stroke-width="1.6"/><circle cx="8" cy="12.3" r="1" fill="currentColor"/></svg>
        +965 66307852
      </li>
      <li>
        <svg viewBox="0 0 16 16"><path d="M3 2h3l1.5 3.5-2 1.2a8 8 0 0 0 3.8 3.8l1.2-2L14 10v3a1.5 1.5 0 0 1-1.5 1.5A11 11 0 0 1 1.5 3.5 1.5 1.5 0 0 1 3 2z" fill="currentColor"/></svg>
        +965 22486037
      </li>
      <li>
        <svg viewBox="0 0 16 16"><rect x="1" y="3" width="14" height="10" rx="1.2" fill="none" stroke="currentColor" stroke-width="1.6"/><path d="M1.5 4l6.5 5 6.5-5" fill="none" stroke="currentColor" stroke-width="1.6"/></svg>
        info@sawtarin.net
      </li>
      <li class="pair">
        <span><i class="dot"></i>@sawtarin</span>
        <span><i class="dot round"></i>@sawtarin</span>
      </li>
    </ul>
    <div class="band"></div>
  </section>

  <section class="card card--back">
    <div class="band"></div>
    <div class="address">
      <span>Office no. 3, 1st floor, Almarfa Complex,</span>
      <span>Rashed AlQeblawi St., Salmiya, Kuwait</span>
    </div>
    <div class="brand">
      <span class="brand-mark"></span>
      <div class="brand-name">SAWTARIN</div>
      <div class="brand-tag">DJ - Sound Eng. - Lighting</div>
      <div class="brand-tag-ar">دي جي - هندسة صوت - إضاءة</div>
    </div>
  </section>
</body>
</html>
```